Labeling for Organic Food

we need a label design for

1. Organic Red Rice
2. Organic wild honey

it is going to be the same design in different dimensions.

1. Organic Red Rice
Dimension 1 28*18.5cm
Dimension 2 13.5*8cm

2. Organic Honey
12*6cm
Updates

There is an update in the brief about using the Bhutanese color scheme. Please check it out.

Target Market(s)

people with the concern of health and the environment.

Requirements
Must have
• 1. our logo
• 2. All the info
• 3. A natural feel
• 4. I would prefer minimalistic style
• 5. Please include Bhutanese national colours as attached.

```html
<!DOCTYPE html>
<html lang="en">
<head>
<meta charset="utf-8">
<title>Organic Wild Honey Label</title>
<link href="https://fonts.googleapis.com/css2?family=Patrick+Hand+SC&family=Noto+Sans+SC:wght@400&family=Dancing+Script:wght@500&family=Josefin+Sans:wght@400;600&display=swap" rel="stylesheet">
<style>
  :root {
    --backdrop: #efd4f8;
    --label-purple: #7f4b86;
    --brand-green: #a5d4a5;
    --paper-white: #ffffff;
    --ink-dark: #2b2b2b;
    --shadow: rgba(0, 0, 0, 0.5);
  }
  html, body {
    margin: 0;
    padding: 0;
    width: 1200px;
    height: 1200px;
    overflow: hidden;
    background: var(--backdrop);
  }
  .label {
    position: absolute;
    left: 100px;
    top: 270px;
    width: 1000px;
    height: 660px;
    background: var(--label-purple);
    overflow: hidden;
    box-shadow: 14px 10px 6px var(--shadow);
  }
  .brand-badge {
    position: absolute;
    left: -38px;
    top: -113px;
    width: 256px;
    height: 256px;
    border-radius: 50%;
    background: var(--brand-green);
  }
  .brand-name {
    position: absolute;
    left: 24px;
    top: 28px;
    margin: 0;
    font-family: "Patrick Hand SC", cursive;
    font-size: 34px;
    color: var(--ink-dark);
    letter-spacing: 0.5px;
  }
  .title-plate {
    position: absolute;
    left: 308px;
    top: -60px;
    width: 382px;
    height: 234px;
    border-radius: 50%;
    background: var(--paper-white);
  }
  .product-title {
    position: absolute;
    left: 0;
    width: 1000px;
    top: 18px;
    margin: 0;
    text-align: center;
    font-weight: normal;
    color: var(--ink-dark);
  }
  .product-title .title-en {
    display: block;
    font-family: "Patrick Hand SC", cursive;
    font-size: 40px;
    letter-spacing: 1px;
    line-height: 48px;
  }
  .product-title .title-zh {
    display: block;
    font-family: "Noto Sans SC", sans-serif;
    font-size: 52px;
    line-height: 60px;
    letter-spacing: 1px;
  }
  .story {
    position: absolute;
    left: 0;
    top: 195px;
    width: 1000px;
    margin: 0;
    text-align: center;
    font-family: "Dancing Script", cursive;
    font-size: 25px;
    line-height: 49px;
    color: var(--paper-white);
  }
  .facts {
    position: absolute;
    left: 0;
    width: 1000px;
    top: 546px;
    margin: 0;
    text-align: center;
    font-family: "Josefin Sans", sans-serif;
    font-variant: small-caps;
    font-size: 12.5px;
    line-height: 16.5px;
    color: var(--ink-dark);
  }
  .facts .group-gap { display: block; height: 5px; }
  .net-info {
    position: absolute;
    left: 782px;
    top: 578px;
    margin: 0;
    font-family: "Josefin Sans", sans-serif;
    font-variant: small-caps;
    font-size: 17px;
    line-height: 20px;
    color: var(--ink-dark);
  }
</style>
</head>
<body>
  <section class="label">
    <div class="brand-badge"></div>
    <p class="brand-name">Verdalune</p>

    <div class="title-plate"></div>
    <h1 class="product-title">
      <span class="title-en">Organic Wild Honey</span>
      <span class="title-zh">有机野生蜂蜜</span>
    </h1>

    <p class="story">
      Organic Wild Honey is freshly collected from the remote<br>
      unpolluted lands of the Himalayans in Bhutan.<br>
      The bees are not fed sugar and antibiotics<br>
      and the honey is free from chemical<br>
      preservatives, coloring and additives.<br>
      The wild honey is not heat treated and unprocessed<br>
      to retain the optimum level of nutritional value and enzymes
    </p>

    <p class="facts">
      Store in a cool and dry place<br>
      Ingredients: Organic Bhutanese Wild Honey<br>
      <span class="group-gap"></span>
      Product of Bhutan<br>
      Distributed by Verdalune<br>
      42 Meadow Lane Riverton 104233
    </p>

    <p class="net-info">
      Net Weight 500ml<br>
      Best before 31/12/19
    </p>
  </section>
</body>
</html>
```